seeking a modern Business Card design for Roof Plumbering Business

hallowell roof plumbing is a local metal re-roof and new construction specialist. We are seeking a modern business card to assist with networking within the industry. Our services are predominantly the installation of metal roofs on new houses, however we also do re-roofs when an existing roof needs replacing. We service both residential and commercial properties. Please include the below details on the card:
Name: Owen Hallowell
Phone: 0417 382 965
Email: owenhallowellroofing@maildrop-example.com

Residential & Commercial
Re-roof & New Construction
Fully Insured

I have uploaded our business logo, which we think would suit a black background. Please use all lower case for business name.
Cheers
Updates

Hey Guys, As requested I've uploaded a Pdf version of my logo. Hopefully this help. Thanks

Industry/Entity Type

Business

Contact Information for Business Card

Name: Owen Hallowell
Phone: 0417 382 965

Residential & Commercial
Fully Insured

Font styles to use
Serif
Sans Serif

Requirements
Must have
• Name must be all lower case "hallowell roof plumbing"
Nice to have
• Stick with Logo Colours

```html
<!DOCTYPE html>
<html lang="en">
<head>
<meta charset="utf-8">
<title>hallowell roof plumbing – business card</title>
<link href="https://fonts.googleapis.com/css2?family=Roboto+Condensed:wght@400;700&display=swap" rel="stylesheet">
<style>
  :root {
    --backdrop: #d9d9d9;
    --card: #232122;
    --brand-blue: #29abe2;
    --text-light: #ffffff;
    --text-band: #ffffff;
  }
  html, body {
    margin: 0;
    padding: 0;
    width: 1200px;
    height: 800px;
    overflow: hidden;
    background: var(--backdrop);
  }
  .canvas {
    width: 1200px;
    height: 800px;
    display: flex;
    align-items: center;
    justify-content: center;
  }
  .business-card {
    position: relative;
    width: 900px;
    height: 540px;
    background: var(--card);
    border-radius: 40px;
    font-family: "Roboto Condensed", "Arial Narrow", sans-serif;
    color: var(--text-light);
    overflow: hidden;
  }
  .brand {
    position: absolute;
    top: 120px;
    left: 0;
    right: 0;
    display: flex;
    align-items: center;
    justify-content: center;
    gap: 18px;
  }
  .brand-square {
    width: 34px;
    height: 34px;
    background: var(--brand-blue);
  }
  .brand-name {
    font-size: 62px;
    font-weight: 400;
    color: var(--brand-blue);
    letter-spacing: 1px;
    line-height: 1;
  }
  .services-band {
    position: absolute;
    top: 258px;
    left: 0;
    right: 0;
    height: 52px;
    background: var(--brand-blue);
    display: flex;
    align-items: center;
    justify-content: center;
    font-size: 27px;
    color: var(--text-band);
    text-transform: uppercase;
    letter-spacing: 0.2px;
  }
  .holder-name {
    position: absolute;
    top: 352px;
    left: 0;
    right: 0;
    text-align: center;
    font-size: 52px;
    font-weight: 700;
    text-transform: uppercase;
    line-height: 1;
  }
  .contact-row {
    position: absolute;
    top: 450px;
    left: 0;
    right: 0;
    display: flex;
    justify-content: center;
    gap: 40px;
    font-size: 32px;
  }
  .contact-item {
    display: flex;
    align-items: center;
    gap: 12px;
  }
  .contact-icon {
    width: 30px;
    height: 30px;
    flex: none;
  }
</style>
</head>
<body>
<main class="canvas">
  <section class="business-card">
    <div class="brand">
      <span class="brand-square"></span>
      <span class="brand-name">hallowell roof plumbing</span>
    </div>

    <div class="services-band">Residential &amp; Commercial • Re-roof &amp; New Construction • Fully Insured</div>

    <h1 class="holder-name" style="margin:0">Owen Hallowell</h1>

    <div class="contact-row">
      <div class="contact-item">
        <svg class="contact-icon" viewBox="0 0 30 30" aria-hidden="true">
          <circle cx="15" cy="15" r="13" fill="none" stroke="var(--brand-blue)" stroke-width="2.5"/>
          <path d="M10 9 l3 -1 2 4 -2 1.5 q1.5 3 4 4.5 l1.5 -2 4 2 -1 3 q-6 0 -11.5 -12z" fill="var(--brand-blue)"/>
        </svg>
        <span class="contact-text">0417 382 965</span>
      </div>
      <div class="contact-item">
        <svg class="contact-icon" viewBox="0 0 30 30" aria-hidden="true">
          <rect x="2" y="7" width="26" height="17" fill="none" stroke="var(--brand-blue)" stroke-width="2.5"/>
          <path d="M2 7 L15 17 L28 7 M2 24 L11 14 M28 24 L19 14" fill="none" stroke="var(--brand-blue)" stroke-width="2.5"/>
        </svg>
        <span class="contact-text">owenhallowellroofing@maildrop-example.com</span>
      </div>
    </div>
  </section>
</main>
</body>
</html>
```